Rioja winery needs a new label design

A family-owned winery in Spain's Rioja Oriental region is looking to create a new label for a wine named "Zunad" Arabic for Castle, that reflects the land from which the wine is born. From the remote village of Quel, La Rioja Oriental, with the backdrop of the Sierra Yerga mountains and the Barrio de Bodegas, or group of caves where locals have produced wines for centuries. Wine name:
2018 Zunad Rioja Tempranillo
Quel, Rioja Oriental
Spain

Font styles to use
Serif
Sans Serif
Decorative
Script

Requirements
Must have
• vines, vineyards, grapes
Nice to have
• mountains,
Should not have
• castles. we already have a label design with the castle

```html
<!DOCTYPE html>
<html lang="en">
<head>
<meta charset="utf-8">
<title>Zunad Rioja Tempranillo 2018 – Label</title>
<link rel="stylesheet" href="https://fonts.googleapis.com/css2?family=Cinzel:wght@400;500;600&family=Cormorant+Garamond:wght@500;600&display=swap">
<style>
  :root {
    --backdrop: #cfcfcf;
    --paper: #f1f1f0;
    --ink: #4f4f4f;
    --ink-soft: #6a6a6a;
    --gold: #b88a22;
    --gold-light: #e6c04e;
    --gold-deep: #a87a16;
    --land-dark: #262626;
    --land-light: #b9b9b9;
  }
  * { margin: 0; padding: 0; box-sizing: border-box; }
  html, body {
    width: 750px;
    height: 1200px;
    overflow: hidden;
    background: var(--backdrop);
  }
  .canvas {
    position: relative;
    width: 750px;
    height: 1200px;
  }
  .label {
    position: absolute;
    left: 65px;
    top: 35px;
    width: 620px;
    height: 1130px;
  }
  .label-shape {
    position: absolute;
    inset: 0;
    width: 620px;
    height: 1130px;
    display: block;
  }
  .label-text {
    position: absolute;
    left: 0;
    width: 620px;
    text-align: center;
    color: var(--ink);
  }
  .wine-name {
    top: 200px;
    font-family: "Cinzel", serif;
    font-weight: 500;
    font-size: 66px;
    letter-spacing: 1px;
    color: var(--gold);
    line-height: 1;
    padding-left: 14px;
  }
  .appellation {
    top: 310px;
    font-family: "Cinzel", serif;
    font-weight: 400;
    font-size: 40px;
    line-height: 1.0;
    padding-left: 14px;
  }
  .vintage {
    top: 582px;
    font-family: "Cormorant Garamond", serif;
    font-weight: 600;
    font-size: 36px;
    color: var(--ink-soft);
    padding-left: 14px;
  }
  .origin {
    top: 660px;
    font-family: "Cinzel", serif;
    font-weight: 400;
    font-size: 23px;
    line-height: 1.0;
    color: var(--ink-soft);
    padding-left: 14px;
  }
</style>
</head>
<body>
  <main class="canvas">
    <article class="label">
      <svg class="label-shape" viewBox="0 0 620 1130" xmlns="http://www.w3.org/2000/svg">
        <defs>
          <linearGradient id="gold-foil" x1="0" y1="0" x2="1" y2="1">
            <stop offset="0" stop-color="var(--gold-deep)"/>
            <stop offset="0.5" stop-color="var(--gold-light)"/>
            <stop offset="1" stop-color="var(--gold)"/>
          </linearGradient>
          <linearGradient id="land-tone" x1="0" y1="0" x2="0.4" y2="1">
            <stop offset="0" stop-color="var(--land-dark)"/>
            <stop offset="0.55" stop-color="#4a4a4a"/>
            <stop offset="1" stop-color="var(--land-light)"/>
          </linearGradient>
        </defs>
        <rect class="gold-band" x="0" y="43" width="320" height="280" fill="url(#gold-foil)"/>
        <path class="paper" d="M0,306 C70,170 250,30 620,0 L620,1130 L0,1130 Z" fill="var(--paper)"/>
        <rect class="landscape" x="0" y="780" width="620" height="350" fill="url(#land-tone)"
              role="img" aria-label="Black and white engraving of the vineyard plain near Quel with the Sierra Yerga mountains and hillside wine caves"/>
      </svg>
      <h1 class="label-text wine-name">Zunad</h1>
      <p class="label-text appellation">Rioja<br>Tempranillo</p>
      <p class="label-text vintage">2018</p>
      <p class="label-text origin">Quel, Rioja Oriental<br>Spain</p>
    </article>
  </main>
</body>
</html>
```